Business Card for a new businees.

need a very good business for a new company based in Riverside California call Levy Lantern LLC. We help client file taxes, resolve tax debt and attain peace of mind We help people nationwide solve Tax problems. We help with Installment agreements, Offers in Compromise, Partial Pay Installment Agreements, Currently Not Collectible status, Liens and Levy Removal, Garnishment removal. We offer individualized services

Target Market(s)

Any one with Tax Problems nationwide. My clients span across age, occupation etc

Contact Information for Business Card

Card must be attractive and have enough information to let client know we care and call us

Colors

Designer to choose colors to be used in the design.

Requirements
Must have
• the basics and then surprise me
Nice to have
• surprise m

```html
<!DOCTYPE html>
<html lang="en">
<head>
<meta charset="utf-8">
<title>Levy Lantern LLC – Business Card</title>
<link href="https://fonts.googleapis.com/css2?family=Roboto:wght@400;500&display=swap" rel="stylesheet">
<style>
  :root {
    --bg: #5a4d46;
    --card: #141414;
    --card-edge: #1d1d1d;
    --gold: #e6c22b;
    --gold-deep: #a88c25;
    --gold-muted: #b89a3a;
    --white: #f4f4f4;
  }
  * { box-sizing: border-box; margin: 0; padding: 0; }
  html, body { width: 1200px; height: 716px; overflow: hidden; }
  body {
    background: var(--bg);
    font-family: "Roboto", Arial, sans-serif;
    position: relative;
  }
  .card {
    position: absolute;
    width: 540px;
    height: 309px;
    background: var(--card);
    border: 1px solid var(--card-edge);
    box-shadow: 0 10px 24px rgba(0,0,0,.45);
    overflow: hidden;
  }
  .card--back { left: 30px; top: 204px; }
  .card--front { left: 630px; top: 204px; }

  /* back side */
  .back-brand {
    position: absolute; left: 0; right: 0; top: 112px;
    display: flex; align-items: center; justify-content: center; gap: 12px;
  }
  .brand-dot { width: 18px; height: 18px; border-radius: 50%; background: var(--gold); }
  .brand-name { color: var(--gold); font-weight: 500; font-size: 34px; letter-spacing: .5px; }
  .back-web {
    position: absolute; left: 0; right: 0; top: 196px;
    text-align: center; color: var(--gold); font-size: 17px; letter-spacing: .4px;
  }

  /* front side */
  .front-brand {
    position: absolute; right: 32px; top: 40px;
    display: flex; flex-direction: column; align-items: flex-end;
  }
  .front-brand .lockup { display: flex; align-items: center; gap: 9px; }
  .front-brand .brand-dot { width: 13px; height: 13px; }
  .front-brand .brand-name { font-size: 25px; }
  .tagline { color: var(--gold-muted); font-size: 7.5px; letter-spacing: 1.6px; margin-top: 5px; }
  .tagline-sub { color: var(--gold-deep); font-size: 5.5px; letter-spacing: .6px; margin-top: 2px; }

  .person { position: absolute; left: 30px; top: 104px; }
  .person-name { color: var(--gold); font-size: 18px; font-weight: 500; }
  .person-title { color: var(--gold-muted); font-size: 14px; margin-top: 2px; }
  .rule {
    position: absolute; left: 150px; right: 30px; top: 140px;
    height: 2px; background: var(--gold);
  }

  .contacts { position: absolute; left: 30px; top: 160px; list-style: none; }
  .contacts li {
    display: flex; align-items: center; gap: 7px;
    color: var(--white); font-size: 13.5px; line-height: 19px;
  }
  .contacts svg { width: 11px; height: 11px; fill: var(--gold); flex: none; }

  .address {
    position: absolute; left: 346px; right: 14px; top: 222px;
    color: var(--white); font-size: 14px; line-height: 20px;
    white-space: nowrap;
  }
  .band { position: absolute; bottom: 0; height: 20px; }
  .band--bright { left: 0; width: 338px; background: var(--gold); }
  .band--deep { left: 346px; right: 0; background: var(--gold-deep); }
</style>
</head>
<body>

  <section class="card card--back" aria-label="Card back">
    <div class="back-brand">
      <span class="brand-dot"></span>
      <span class="brand-name">Levy Lantern</span>
    </div>
    <p class="back-web">www.levylantern.com</p>
  </section>

  <section class="card card--front" aria-label="Card front">
    <div class="front-brand">
      <div class="lockup">
        <span class="brand-dot"></span>
        <span class="brand-name">Levy Lantern</span>
      </div>
      <p class="tagline">TAX RELIEF. TAX RETURNS.</p>
      <p class="tagline-sub">YOUR TAX ADVOCATES. WE HANDLE EVERY TAX MATTER</p>
    </div>

    <div class="person">
      <p class="person-name">Employee Name</p>
      <p class="person-title">Title</p>
    </div>
    <div class="rule"></div>

    <ul class="contacts">
      <li>
        <svg viewBox="0 0 24 24" aria-hidden="true"><path d="M6.6 10.8a15.1 15.1 0 0 0 6.6 6.6l2.2-2.2a1 1 0 0 1 1-.25 11.4 11.4 0 0 0 3.6.57 1 1 0 0 1 1 1V20a1 1 0 0 1-1 1A17 17 0 0 1 3 4a1 1 0 0 1 1-1h3.5a1 1 0 0 1 1 1c0 1.25.2 2.45.57 3.570a1 1 0 0 1-.25 1z"/></svg>
        951-555-0148
      </li>
      <li>
        <svg viewBox="0 0 24 24" aria-hidden="true"><path d="M7 1h10a2 2 0 0 1 2 2v18a2 2 0 0 1-2 2H7a2 2 0 0 1-2-2V3a2 2 0 0 1 2-2zm0 3v14h10V4zm5 15.2a1 1 0 1 0 0 2 1 1 0 0 0 0-2z"/></svg>
        951-555-0148
      </li>
      <li>
        <svg viewBox="0 0 24 24" aria-hidden="true"><path d="M2 5h20v14H2zm2 2v.5l8 5 8-5V7zm0 2.8V17h16V9.8l-8 5z"/></svg>
        info@levylantern.com
      </li>
      <li>
        <svg viewBox="0 0 24 24" aria-hidden="true"><path d="M12 2a10 10 0 1 0 0 20 10 10 0 0 0 0-20zm6.9 6h-3a15 15 0 0 0-1.3-3.9A8 8 0 0 1 18.9 8zM12 4a13 13 0 0 1 1.9 4h-3.8A13 13 0 0 1 12 4zM4.3 14a8 8 0 0 1 0-4h3.4a16 16 0 0 0 0 4zm.8 2h3a15 15 0 0 0 1.3 3.9A8 8 0 0 1 5.1 16zm3-8h-3a8 8 0 0 1 4.3-3.9A15 15 0 0 0 8.1 8zM12 20a13 13 0 0 1-1.9-4h3.8A13 13 0 0 1 12 20zm2.3-6H9.7a14 14 0 0 1 0-4h4.6a14 14 0 0 1 0 4zm.3 5.9a15 15 0 0 0 1.3-3.9h3a8 8 0 0 1-4.3 3.9zm1.7-5.9a16 16 0 0 0 0-4h3.4a8 8 0 0 1 0 4z"/></svg>
        www.levylantern.com
      </li>
    </ul>

    <p class="address">4270 Orchard Ave. Ste 310<br>Riverside, CA 92501</p>

    <div class="band band--bright"></div>
    <div class="band band--deep"></div>
  </section>

</body>
</html>
```